Website design for a Fine Food exhibition in Asia

We need a website design for a Food and Wine exhibition (home page). The name of the exhibition is "Platara" which is going to be Held in south korea. The concept is "Fine Food" in major, qui means clustering Would not we accept Any canned food, fast food, chips, thesis kind of foods. We do not open to the public like Some Other Food exhibitions do, Then only trade visitors. The EXHIBITORS will come from all the World. The categories we Would like to make is in attachment below. We will update the text When the category's share will be done. We need a color can qui correspond well to the "Find Food ', color of our logo qui est in attachment Would be good. You can offer us some photos, images, like photos of fine food corners in supermarkets, gourmet shops like photos of etc. ... You can find links Some of "same" exhibitions in below, qui can give you a guideline of the kind of website we expect. http://en.vitrine-delices-choix.example/ http://marblerootfair.example/ http: //www.tideplatenexpo. example.kr We will ask to the winning designer to Develop the full website under Wordpress.

Target Market(s)

Fine food, gourmet food, "grocery", pastry, bakery

Number of Pages Required

5+ page

Font styles to use
Sans Serif

Colors
886aae
6b449b
e34197
e667a6
9bcb3c
f58947
f37122
ec1f27

Requirements
Must have
• Warm colors, and layout showing the high level of foods, fine foods, gourmet foods
Nice to have
• It would be nice to include the sentence "The new meeting place for the gourmet food in Asia"

```html
<!DOCTYPE html>
<html lang="en">
<head>
<meta charset="utf-8">
<title>Platara – The Fine Food Event in Asia</title>
<link href="https://fonts.googleapis.com/css2?family=Roboto:wght@400;500;700&display=swap" rel="stylesheet">
<style>
:root{
  --plum:#670a68;
  --ink:#333333;
  --muted:#555555;
  --white:#ffffff;
  --rule:#cfcdd3;
}
*{box-sizing:border-box;margin:0;padding:0}
html,body{width:1200px;height:2844px;overflow:hidden}
body{position:relative;font-family:'Roboto',Arial,sans-serif;color:var(--ink);background:var(--white)}
.abs{position:absolute}
.topbar{left:0;top:0;width:1200px;height:38px;background:var(--plum);color:var(--white);font-size:15px}
.topbar .mail{left:85px;top:10px;display:flex;align-items:center;gap:10px}
.topbar .signin{right:85px;top:10px;display:flex;align-items:center;gap:10px;font-weight:500}
.nav{left:0;top:38px;width:1200px;height:92px;background:var(--white)}
.nav span{position:absolute;top:36px;font-size:15px;color:#444}
.nav span.active{color:var(--plum);font-weight:500}
.brand{left:504px;top:12px;width:136px;height:136px;border-radius:50%;background:var(--white);border:5px solid var(--plum);display:flex;align-items:center;justify-content:center;z-index:5;color:var(--plum);font-weight:700;font-size:28px}
.hero{left:0;top:130px;width:1200px;height:520px;background:radial-gradient(ellipse at 45% 55%,#7b8a4a 0%,#5a4a34 35%,#2a2420 70%,#151312 100%)}
.hero-title{left:0;top:335px;width:1200px;text-align:center;color:var(--white);font-size:42px;font-weight:500;line-height:50px;text-shadow:0 2px 6px rgba(0,0,0,.5)}
.arrow{top:370px}
.fact{position:absolute;top:570px;width:184px;height:184px;border-radius:50%;background:radial-gradient(circle at 50% 40%,#f7f4ef 0%,#e9e1d6 70%,#d8cbbc 100%);box-shadow:0 4px 10px rgba(0,0,0,.15);text-align:center;font-size:11px;color:#444;padding-top:56px;line-height:20px}
.fact svg{display:block;margin:0 auto 6px}
.section-title{left:0;width:1200px;text-align:center;font-size:27px;font-weight:400;color:#333}
.divider{left:510px;width:180px;height:14px}
.welcome-text{left:275px;top:872px;width:650px;text-align:center;font-size:13px;line-height:22px;color:var(--muted)}
.btn{position:absolute;display:flex;align-items:center;justify-content:center;font-size:13px;text-transform:uppercase;background:var(--plum);color:var(--white);box-shadow:inset 0 0 0 2px var(--plum),inset 0 0 0 3px rgba(255,255,255,.6)}
.btn.light{background:var(--white);color:#333;box-shadow:none}
.snack{left:935px;top:845px;width:205px;height:232px;background:radial-gradient(circle at 35% 25%,#c8621d 0,#9c4212 22%,rgba(255,255,255,0) 36%),radial-gradient(ellipse at 75% 80%,#e9c3a8 0,#e9c3a8 25%,rgba(255,255,255,0) 50%)}
.audience{left:0;top:1077px;width:1200px;height:417px;background:radial-gradient(ellipse at 60% 40%,#3e2a1e 0%,#241a15 50%,#151110 100%)}
.panel{position:absolute;top:63px;width:360px;height:283px;border:1px solid rgba(255,255,255,.85);color:var(--white);text-align:center}
.panel h2{font-size:27px;font-weight:500;margin-top:56px}
.panel p{font-size:13px;line-height:20px;margin:12px auto 0;width:310px}
.panel .free{font-size:34px;font-weight:500;margin-top:14px}
.news-card{position:absolute;top:1659px;width:287px;height:400px}
.news-card .photo{width:287px;height:241px;border:4px solid var(--white);box-shadow:0 2px 8px rgba(0,0,0,.3)}
.news-card h3{font-size:18px;font-weight:500;margin-top:34px;color:#222;line-height:22px}
.news-card p{font-size:13px;line-height:18px;color:#444;margin-top:4px;width:250px}
.news-card .btn{left:0;top:357px;width:106px;height:33px}
.making{left:0;top:2124px;width:1200px;height:372px;background:radial-gradient(ellipse at 50% 40%,#2e2924 0%,#1c1916 60%,#121110 100%);color:var(--white)}
.making h2{position:absolute;top:72px;width:1200px;text-align:center;font-size:21px;font-weight:500}
.making .lead{position:absolute;top:113px;width:1200px;text-align:center;font-size:12px}
.step{position:absolute;top:219px;width:42px;height:42px;border-radius:50%;background:var(--white);color:#222;font-size:18px;font-weight:700;display:flex;align-items:center;justify-content:center}
.step-label{position:absolute;top:286px;width:240px;text-align:center;font-size:14px}
.footer{left:0;top:2496px;width:1200px;height:348px;background:linear-gradient(135deg,#efeef1 0%,#e4e3e8 50%,#eeedf0 100%)}
.col{position:absolute;top:46px}
.col h4{font-size:21px;font-weight:500;color:var(--plum);margin-bottom:14px}
.col p{font-size:13px;line-height:20px;color:#777}
.socials{display:flex;gap:10px;margin-top:22px}
.socials span{width:34px;height:34px;border:1px solid #666;background:#f5f5f5}
.contact-row{display:flex;align-items:center;gap:16px;margin-bottom:14px;font-size:13px;line-height:17px;color:#888}
.contact-row .ico{flex:none;width:38px;height:38px;border-radius:50%;border:1px solid #777;display:flex;align-items:center;justify-content:center}
.links{list-style:none;font-size:13px;line-height:19px;color:#777}
.links li::before{content:"» ";color:#555}
.email-field{width:238px;height:36px;background:var(--white);border:1px solid #ddd;margin-top:16px;padding:10px 14px;font-size:12px;font-style:italic;color:#888}
.send{position:relative;display:flex;margin-top:8px;width:78px;height:34px;font-size:16px;font-weight:700}
.rule{left:85px;top:268px;width:1030px;height:1px;background:var(--rule)}
.copyright{left:0;top:292px;width:1200px;text-align:center;font-size:13px;color:#666}
</style>
</head>
<body>

<header class="abs topbar">
  <div class="abs mail">
    <svg width="16" height="12" viewBox="0 0 16 12"><rect width="16" height="12" rx="1" fill="#fff"/><path d="M0 1l8 6 8-6" stroke="#670a68" stroke-width="1.5" fill="none"/></svg>
    info@platara-expo.example
  </div>
  <div class="abs signin">
    <svg width="13" height="14" viewBox="0 0 13 14"><circle cx="6.5" cy="4" r="3.5" fill="#fff"/><path d="M0 14c0-4 3-6 6.5-6s6.5 2 6.5 6z" fill="#fff"/></svg>
    SIGN IN
  </div>
</header>

<nav class="abs nav">
  <span class="active" style="left:87px">HOME</span>
  <span style="left:175px">ABOUT PLATARA</span>
  <span style="left:332px">FLOOR PLAN ⌄</span>
  <span style="left:709px">EXHIBITORS</span>
  <span style="left:834px">VISITORS</span>
  <span style="left:942px">NEWS</span>
  <span style="left:1030px">CONTACT US</span>
</nav>
<div class="abs brand">Platara</div>

<section class="abs hero" role="img" aria-label="Plated gourmet salad with grilled chicken and croutons"></section>
<h1 class="abs hero-title">THE NEW MEETING PLACE FOR THE<br>GOURMET FOOD IN ASIA</h1>
<svg class="abs arrow" style="left:28px" width="16" height="28" viewBox="0 0 16 28"><path d="M14 2L3 14l11 12" stroke="#fff" stroke-width="2.5" fill="none"/></svg>
<svg class="abs arrow" style="left:1156px" width="16" height="28" viewBox="0 0 16 28"><path d="M2 2l11 12L2 26" stroke="#fff" stroke-width="2.5" fill="none"/></svg>

<div class="fact" style="left:327px">
  <svg width="18" height="18" viewBox="0 0 18 18"><circle cx="9" cy="9" r="7.5" stroke="#670a68" stroke-width="2" fill="none"/><path d="M9 4v5l3 2" stroke="#670a68" stroke-width="2" fill="none"/></svg>
  10:00 – 18:00 – FIRST DAY<br>10:00 – 17:00 – SECOND DAY
</div>
<div class="fact" style="left:508px">
  <svg width="18" height="18" viewBox="0 0 18 18"><rect x="1" y="3" width="16" height="14" fill="#670a68"/><rect x="3" y="7" width="12" height="8" fill="#f3eee8"/><rect x="4" y="0" width="2" height="5" fill="#670a68"/><rect x="12" y="0" width="2" height="5" fill="#670a68"/></svg>
  02-03 NOVEMBER<br>2017
</div>
<div class="fact" style="left:690px">
  <svg width="20" height="18" viewBox="0 0 20 18"><path d="M10 0L0 5h20z" fill="#670a68"/><rect x="2" y="6" width="3" height="8" fill="#670a68"/><rect x="8.5" y="6" width="3" height="8" fill="#670a68"/><rect x="15" y="6" width="3" height="8" fill="#670a68"/><rect x="0" y="15" width="20" height="3" fill="#670a68"/></svg>
  VENUE<br>MARLOW HALL 8B
</div>

<section class="welcome">
  <h2 class="abs section-title" style="top:793px">WELCOME TO PLATARA</h2>
  <svg class="abs divider" style="top:841px" viewBox="0 0 180 14"><line x1="0" y1="7" x2="70" y2="7" stroke="#670a68"/><line x1="110" y1="7" x2="180" y2="7" stroke="#670a68"/><rect x="85" y="2" width="10" height="10" fill="#670a68" transform="rotate(45 90 7)"/></svg>
  <p class="abs welcome-text">There are many variations of passages of Lorem Ipsum available, but the majority have suffered alteration in some form, by injected humour, or randomised words which don't look even slightly believable. If you are going to use a passage of Lorem Ipsum, you need to be sure there isn't anything embarrassing tend to repeat predefined chunks as necessary, making this the first true generator on the Internet.</p>
  <span class="btn" style="left:534px;top:982px;width:134px;height:42px">Read More</span>
  <div class="abs snack" role="img" aria-label="Hand holding a skewer of glazed grilled meat"></div>
</section>

<section class="abs audience" role="img" aria-label="Dark close-up of gourmet dishes">
  <div class="panel" style="left:222px">
    <h2>EXHIBITORS</h2>
    <p>Lorem Ipsum is not simply random text. It has roots in a piece of classical Latin literature from professor at Harrow Vale College</p>
    <span class="btn light" style="left:36px;top:180px;width:134px;height:42px">Read More</span>
    <span class="btn" style="left:195px;top:180px;width:130px;height:42px">Register Now</span>
  </div>
  <div class="panel" style="left:619px">
    <h2>VISITORS</h2>
    <div class="free">FREE ADMISSION!!</div>
    <span class="btn light" style="left:36px;top:180px;width:134px;height:42px">Learn More</span>
    <span class="btn" style="left:195px;top:180px;width:130px;height:42px">Register Now</span>
  </div>
</section>

<section class="news">
  <h2 class="abs section-title" style="top:1558px">OUR NEWS</h2>
  <svg class="abs divider" style="top:1604px" viewBox="0 0 180 14"><line x1="0" y1="7" x2="70" y2="7" stroke="#670a68"/><line x1="110" y1="7" x2="180" y2="7" stroke="#670a68"/><rect x="85" y="2" width="10" height="10" fill="#670a68" transform="rotate(45 90 7)"/></svg>
  <article class="news-card" style="left:127px">
    <div class="photo" role="img" aria-label="Close-up of a dish with red berries and greens" style="background:radial-gradient(circle at 45% 55%,#b3263a 0%,#6e1a22 45%,#2a0e10 100%)"></div>
    <h3>TITLE HERE</h3>
    <p>Lorem Ipsum generators on the Internet tend to repeat predefined necessary.</p>
    <span class="btn">Read More</span>
  </article>
  <article class="news-card" style="left:455px">
    <div class="photo" role="img" aria-label="Plated grilled meat with tomato and sauce" style="background:radial-gradient(ellipse at 50% 50%,#a2452a 0%,#6a3b24 40%,#d9d0c6 75%,#efe9e2 100%)"></div>
    <h3>TITLE HERE</h3>
    <p>Lorem Ipsum generators on the Internet tend to repeat predefined necessary.</p>
    <span class="btn">Read More</span>
  </article>
  <article class="news-card" style="left:781px">
    <div class="photo" role="img" aria-label="Plated grilled meat with tomato and sauce" style="background:radial-gradient(ellipse at 50% 50%,#a2452a 0%,#6a3b24 40%,#d9d0c6 75%,#efe9e2 100%)"></div>
    <h3>TITLE HERE</h3>
    <p>Lorem Ipsum generators on the Internet tend to repeat predefined necessary.</p>
    <span class="btn">Read More</span>
  </article>
</section>

<section class="abs making" role="img" aria-label="Dark photo of fresh ingredients">
  <h2>HOW WE MADE IT</h2>
  <p class="lead">Morbi sed justo felis. Phasellus condimentum ornare maximus. Nulla convallis tortor</p>
  <svg class="abs" style="left:330px;top:239px" width="520" height="4"><line x1="0" y1="2" x2="520" y2="2" stroke="#fff" stroke-width="2" stroke-dasharray="5 5"/></svg>
  <div class="step" style="left:288px">1</div>
  <div class="step" style="left:548px">2</div>
  <div class="step" style="left:806px">3</div>
  <div class="step-label" style="left:189px">WITH FRESH PRODUCTS</div>
  <div class="step-label" style="left:449px">WITH LOVE</div>
  <div class="step-label" style="left:707px">FEEL IT,FAST IT!</div>
</section>

<footer class="abs footer" role="img" aria-label="Faint street map background">
  <div class="col" style="left:85px;width:250px">
    <h4>ABOUT US</h4>
    <p>Lorem Ipsum repeat generators on the Internet tendt repeat predefined chunks as tendt necessary.</p>
    <div class="socials"><span></span><span></span><span></span><span></span></div>
  </div>
  <div class="col" style="left:389px;width:260px">
    <h4>GET IN TOUCH</h4>
    <div class="contact-row"><span class="ico"><svg width="12" height="16" viewBox="0 0 12 16"><path d="M6 0a6 6 0 0 0-6 6c0 4 6 10 6 10s6-6 6-10a6 6 0 0 0-6-6z" fill="#555"/><circle cx="6" cy="6" r="2" fill="#fff"/></svg></span><span>88 Harbor Row<br>Westfield</span></div>
    <div class="contact-row"><span class="ico"><svg width="15" height="15" viewBox="0 0 15 15"><path d="M3 0l3 3-2 2c1 2 3 4 5 5l2-2 3 3-2 3C7 14 1 8 0 3z" fill="#555"/></svg></span><span>555-010-4821</span></div>
    <div class="contact-row"><span class="ico"><svg width="16" height="12" viewBox="0 0 16 12"><rect width="16" height="12" rx="1" fill="#555"/><path d="M0 1l8 6 8-6" stroke="#fff" stroke-width="1.5" fill="none"/></svg></span><span>info@platara-expo.example</span></div>
  </div>
  <div class="col" style="left:673px;width:180px">
    <h4>QUICK LINKS</h4>
    <ul class="links"><li>Home</li><li>About us</li><li>Floor Plan</li><li>Exhibitors</li><li>Visitors</li><li>News</li><li>Contact us</li></ul>
  </div>
  <div class="col" style="left:876px;width:250px">
    <h4>OUR NEWSLETTER</h4>
    <p>Lorem Ipsum repeat generators on the Internet tendt repeat.</p>
    <div class="email-field">E-mail address...</div>
    <span class="btn send">Send</span>
  </div>
  <div class="abs rule"></div>
  <p class="abs copyright">@copyright 2016 Platara.All Rights Reserved</p>
</footer>

</body>
</html>
```